business card design for luxurious real estate brand

using the attached logo, i am looking for a 2-sided business card design. the back should be the gold logo on black background. the front needs to include: gold logo, name, phone, email, and website

Industry/Entity Type

real estate

Contact Information for Business Card

logo, name, email, phone, website

Font styles to use
Sans Serif

```html
<!DOCTYPE html>
<html lang="en">
<head>
<meta charset="utf-8">
<title>Harbor Crest – Business Cards</title>
<link href="https://fonts.googleapis.com/css2?family=Montserrat:wght@400;500;600&display=swap" rel="stylesheet">
<style>
  :root {
    --bg: #6e6f71;
    --card: #151515;
    --card-back: #121212;
    --gold: #ffcc0a;
    --white: #f2f2f2;
    --mark-dark: #2a2a2a;
  }
  * { margin: 0; padding: 0; box-sizing: border-box; }
  html, body { width: 1200px; height: 781px; overflow: hidden; }
  body {
    background: radial-gradient(ellipse at 40% 40%, #8a8b8d 0%, var(--bg) 70%);
    font-family: "Montserrat", sans-serif;
    position: relative;
  }
  .card {
    position: absolute;
    top: 247px;
    width: 500px;
    height: 286px;
    border-radius: 16px;
    overflow: hidden;
    box-shadow: 0 18px 40px rgba(0,0,0,.35);
  }
  .card--front { left: 60px; background: var(--card); }
  .card--back { left: 640px; background: var(--card-back); display: flex; align-items: center; justify-content: center; }

  .front-accent {
    position: absolute; left: 0; right: 0; bottom: 0; height: 7px;
    background: var(--gold);
  }
  .brand {
    display: flex; align-items: center; gap: 12px;
    font-weight: 600; font-size: 24px; letter-spacing: 2px;
    text-transform: uppercase; color: var(--gold);
    white-space: nowrap;
  }
  .brand-square { width: 18px; height: 18px; background: var(--gold); }
  .card--front .brand { position: absolute; top: 66px; left: 0; right: 0; justify-content: center; }
  .card--back .brand { color: var(--mark-dark); font-size: 28px; }
  .card--back .brand-square { background: var(--mark-dark); width: 22px; height: 22px; }

  .details {
    position: absolute; left: 34px; right: 30px; bottom: 48px;
    display: flex; align-items: center; gap: 22px;
  }
  .person { text-align: right; min-width: 170px; }
  .person-name {
    font-weight: 500; font-size: 19px; color: var(--gold);
    text-transform: uppercase; letter-spacing: .5px; white-space: nowrap;
  }
  .person-title { font-size: 12px; color: var(--white); margin-top: 3px; }
  .divider { width: 1.5px; height: 66px; background: var(--white); }
  .contacts { list-style: none; display: flex; flex-direction: column; gap: 6px; }
  .contact {
    display: flex; align-items: center; gap: 9px;
    font-size: 12.5px; color: var(--white); letter-spacing: .3px; white-space: nowrap;
  }
  .contact svg { width: 12px; height: 12px; fill: var(--gold); flex: none; }
</style>
</head>
<body>
  <section class="card card--front" aria-label="Business card front">
    <div class="brand"><span class="brand-square"></span>Harbor Crest</div>
    <div class="details">
      <div class="person">
        <p class="person-name">Daniel Marston</p>
        <p class="person-title">Director</p>
      </div>
      <div class="divider"></div>
      <ul class="contacts">
        <li class="contact">
          <svg viewBox="0 0 24 24" aria-hidden="true"><path d="M6.6 10.8a15 15 0 0 0 6.6 6.6l2.2-2.2a1 1 0 0 1 1-.25 11.4 11.4 0 0 0 3.6.57 1 1 0 0 1 1 1V20a1 1 0 0 1-1 1A17 17 0 0 1 3 4a1 1 0 0 1 1-1h3.5a1 1 0 0 1 1 1c0 1.25.2 2.45.57 3.6a1 1 0 0 1-.25 1z"/></svg>
          82-10-4820-3915
        </li>
        <li class="contact">
          <svg viewBox="0 0 24 24" aria-hidden="true"><path d="M2 5h20v14H2zm2 2v.5l8 5 8-5V7z"/></svg>
          info@ridgewellhomes.com
        </li>
        <li class="contact">
          <svg viewBox="0 0 24 24" aria-hidden="true"><circle cx="12" cy="12" r="10"/></svg>
          www.ridgewellhomes.com
        </li>
      </ul>
    </div>
    <div class="front-accent"></div>
  </section>

  <section class="card card--back" aria-label="Business card back">
    <div class="brand"><span class="brand-square"></span>Harbor Crest</div>
  </section>
</body>
</html>
```